Private Labeling Project for Salon

We have created as sunless solution that we would like to bottle and sell. The last thing we need is a label for the bottle. I attached some Designs for inspiration. I also attached a label of another companies tanning solution so you can have a good idea of the size it will be.
The size of the label will be approximately 4"x6". Its going on the outside of a gallon container.
I would like the design to be modern and chic. I would like it to be clean. less is more

Label needs to have logo, ingredients, warnings, and icon for not tested on animals and recycle.
Ingredients: Aqua,Grapefruit seed extract,dihydroxyacetone,green tea extract,Erythrulose,Aloe barbadensis gel,glycerin,polysorbate 20
Phenoxyethanol,FD&C Blue 1,FD&C,Yellow 5,FD&C Red 40,FD&C Green 3,Citric Acid,Fragrance

Warning : This product does not contain sunscreens and does not protect against sunburn. UV-exposure can lead to skin cancer and premature aging, even if you don’t burn.

Manufactured Exclusively by:

Brook, Incorporated
Harlow, Ohio USA
Brookvarn.com

Industry/Entity Type

Beauty Salon

Font styles to use
Sans Serif

Colors
000000
ffffff
c3c3c3

Requirements
Must have
• All file types for
• the Label needs to have:
• Since we make 5 types of solution each label needs to have 4 check boxes one for:
• 5%
• 8%
• 9%
• 11%
• Rapid Tan
• logo, ingredients, warnings, and icon for not tested on animals and recycle.
• Ingredients: Aqua,Grapefruit seed extract,dihydroxyacetone,green tea extract,Erythrulose,Aloe barbadensis gel,glycerin,polysorbate 20
• Phenoxyethanol,FD&C Blue 1,FD&C,Yellow 5,FD&C Red 40,FD&C Green 3,Citric Acid,Fragrance
• Warning : This product does not contain sunscreens and does not protect against sunburn. UV-exposure can lead to skin cancer and premature aging, even if you don’t burn.
• Manufactured Exclusively by:
• Brook, Incorporated
• Harlow, Ohio USA
• Brookvarn.com

```html
<!DOCTYPE html>
<html lang="en">
<head>
<meta charset="utf-8">
<title>Brook Sunless Solution Label</title>
<link href="https://fonts.googleapis.com/css2?family=Jost:wght@400;600&family=Lato:wght@300;400&display=swap" rel="stylesheet">
<style>
  :root {
    --ink: #000000;
    --paper: #ffffff;
    --rule: #c3c3c3;
  }
  html, body {
    margin: 0;
    padding: 0;
    width: 1200px;
    height: 1000px;
    overflow: hidden;
    background: var(--paper);
  }
  .canvas {
    position: relative;
    width: 1200px;
    height: 1000px;
  }
  .label {
    position: absolute;
    left: 300px;
    top: 50px;
    width: 600px;
    height: 900px;
    background: var(--ink);
    color: var(--paper);
  }
  .brand {
    position: absolute;
    top: 196px;
    left: 0;
    width: 100%;
    text-align: center;
    font-family: "Jost", sans-serif;
    font-weight: 400;
    font-size: 72px;
    letter-spacing: 0.22em;
    line-height: 1;
    padding-left: 0.22em;
    box-sizing: border-box;
  }
  .product-name {
    position: absolute;
    top: 412px;
    left: 0;
    width: 100%;
    margin: 0;
    text-align: center;
    font-family: "Jost", sans-serif;
    font-weight: 600;
    font-size: 56px;
    line-height: 1.1;
    letter-spacing: 0.01em;
  }
  .maker {
    position: absolute;
    top: 648px;
    left: 0;
    width: 100%;
    text-align: center;
    font-family: "Lato", sans-serif;
    font-weight: 300;
    line-height: 1.1;
  }
  .maker-intro {
    font-size: 13px;
    margin: 0 0 6px;
    color: var(--rule);
  }
  .maker-details {
    font-size: 19px;
    margin: 0;
    color: var(--paper);
  }
  .divider {
    position: absolute;
    top: 758px;
    left: 36px;
    width: 528px;
    height: 0;
    border-top: 2px solid var(--paper);
  }
  .fine-print {
    position: absolute;
    left: 36px;
    top: 776px;
    width: 520px;
    font-family: "Lato", sans-serif;
    font-weight: 400;
    font-size: 10.5px;
    line-height: 1.4;
  }
  .fine-print p { margin: 0 0 12px; }
  .fine-print .warning { width: 470px; }
  .recycle-icon {
    position: absolute;
    left: 528px;
    top: 826px;
    width: 34px;
    height: 34px;
  }
</style>
</head>
<body>
<main class="canvas">
  <section class="label">
    <div class="brand">BROOK</div>
    <h1 class="product-name">SUNLESS<br>SOLUTION</h1>
    <div class="maker">
      <p class="maker-intro">Manufactured Exclusively by:</p>
      <p class="maker-details">Brook, Incorporated<br>Harlow, Ohio USA<br>Brookvarn.com</p>
    </div>
    <div class="divider"></div>
    <div class="fine-print">
      <p>Ingredients: Aqua, Grapefruit seed extract, dihydroxyacetone, green tea extract, Erythrulose, Aloe barbadensis gel, glycerin, polysorbate 20, Phenoxyethanol, Citric Acid, Fragrance.</p>
      <p class="warning">Warning : This product does not contain sunscreens and does not protect against sunburn. UV-exposure can lead to skin cancer and premature aging, even if you don’t burn.</p>
    </div>
    <svg class="recycle-icon" viewBox="0 0 40 40" role="img" aria-label="Recycle">
      <defs>
        <marker id="arrow-head" viewBox="0 0 10 10" refX="4" refY="5" markerWidth="3" markerHeight="3" orient="auto">
          <path d="M0 0 L10 5 L0 10 Z" fill="#ffffff"/>
        </marker>
      </defs>
      <g fill="none" stroke="#ffffff" stroke-width="4.5" stroke-linecap="butt" marker-end="url(#arrow-head)">
        <path d="M7 30 L15 16"/>
        <path d="M22 7 L30 21"/>
        <path d="M33 35 L17 35"/>
      </g>
    </svg>
  </section>
</main>
</body>
</html>
```